PEACFUL ACUPUNCTURE PRACTITIONER NEEDS A NEW COAT

I need a new design for an exiting website http://willowgateneedlework.com/ for a acupuncturist. This will be a minimalism design with lots and lots of white space. Home page and one interior page. Please keep the feeling of calm and peaceful serenity. For Color scheme: https://www.morningfernclinic.com/fertility. The bottom part of the home page with sections and links to the service pages: https://harborlotuswellness.com/. The client likes this the best: http://mfclinic.com/. I'm attaching the logo and content pages.

Target Market(s)

Women

Industry/Entity Type

Wellness, health, wellbeing, meditation

Number of Pages Required

2 page

Font styles to use
Sans Serif
Decorative

Colors

Designer to choose colors to be used in the design.

Requirements
Must have
Nice to have
• Follow new website drafts and links
Should not have
• Busy with bright colors. No poping

```html
<!DOCTYPE html>
<html lang="en">
<head>
<meta charset="utf-8">
<title>Stillwater Acupuncture</title>
<link href="https://fonts.googleapis.com/css2?family=Poppins:ital,wght@0,300;0,400;0,500;0,600;1,300;1,400&family=Alice&display=swap" rel="stylesheet">
<style>
:root{
  --ink:#4a4a4a;
  --text:#5b5b5b;
  --muted:#8a8a8a;
  --rose:#b98a92;
  --rose-soft:#d9c0c3;
  --blush:#f2eeed;
  --sand:#e6dcd9;
  --line:#e8e4e3;
  --gold:#f5b400;
  --gold-pale:#f6e6b8;
  --white:#fff;
}
*{margin:0;padding:0;box-sizing:border-box}
html,body{width:1200px;height:3446px;overflow:hidden;background:var(--white)}
body{position:relative;font-family:'Poppins',sans-serif;color:var(--text)}
.abs{position:absolute}
.band{position:absolute;left:0;width:1200px;background:var(--blush)}
.social{display:flex;gap:10px}
.social span{width:34px;height:34px;border-radius:50%;background:#f1f1f1;display:block}
.brand{display:flex;align-items:center;gap:12px;color:var(--ink)}
.brand .mark{width:46px;height:46px;border-radius:50%;background:var(--rose-soft)}
.brand .name{font-family:'Alice',serif;font-size:30px;line-height:1;letter-spacing:.5px}
.brand .name small{display:block;font-size:19px;letter-spacing:4px;margin-top:2px}
.nav{position:absolute;left:0;width:1200px;display:flex;justify-content:center;gap:20px;font-size:12.5px;color:var(--ink);letter-spacing:.2px}
.phone{display:flex;align-items:center;gap:10px;font-size:15px;font-weight:500;color:var(--ink)}
.phone i{width:38px;height:38px;border-radius:50%;background:#f1f1f1;display:flex;align-items:center;justify-content:center}
.hero{position:absolute;top:155px;left:0;width:1200px;height:685px;background:linear-gradient(90deg,#f7f7f7 0%,#f4f3f2 40%,#d8d2ce 65%,#a79e98 85%,#8d8681 100%)}
.hero .eyebrow{position:absolute;left:85px;top:126px;font-size:18px;color:var(--ink)}
.hero h1{position:absolute;left:82px;top:165px;font-weight:400;font-size:76px;line-height:70px;color:var(--ink)}
.hero p{position:absolute;left:85px;top:322px;width:400px;font-size:13px;line-height:22px}
.down{position:absolute;left:86px;top:525px;width:80px;height:80px;border-radius:50%;background:#fff;box-shadow:0 10px 30px rgba(0,0,0,.1);display:flex;align-items:center;justify-content:center}
.quote{position:absolute;top:983px;left:200px;width:800px;text-align:center;font-style:italic;font-weight:300;font-size:16.5px;line-height:27px;color:var(--ink)}
.rule{position:absolute;top:1122px;left:88px;width:1012px;height:1px;background:var(--line)}
.h2{position:absolute;left:0;width:1200px;text-align:center;font-weight:400;font-size:46px;color:var(--ink)}
.card{position:absolute;top:1287px;width:246px;height:346px;background:#fff;box-shadow:0 18px 40px rgba(0,0,0,.07);text-align:center}
.card .pic{width:110px;height:110px;border-radius:50%;margin:45px auto 0}
.card h3{margin-top:24px;font-size:16.5px;font-weight:500;color:var(--ink)}
.card p{margin:20px auto 0;width:190px;font-size:13px;line-height:20px}
.about-pic{position:absolute;left:163px;top:1800px;width:400px;height:400px;border-radius:50%;background:radial-gradient(circle,#ead9d6,#dcc6c2)}
.about-figure{position:absolute;left:270px;top:1717px;width:230px;height:515px;border-radius:110px 110px 0 0;background:linear-gradient(180deg,#6a4a3e 0%,#9c8c7d 30%,#a8998a 100%)}
.about .eyebrow{position:absolute;left:642px;top:1784px;font-size:17px;color:var(--ink)}
.about h2{position:absolute;left:641px;top:1806px;font-weight:400;font-size:46px;color:var(--ink)}
.about p{position:absolute;left:642px;top:1876px;width:405px;font-size:13px;line-height:22.4px}
.about a{position:absolute;left:642px;top:2061px;font-size:11.5px;font-weight:500;color:var(--rose);text-decoration:underline}
.dots{position:absolute;left:939px;top:2171px;display:grid;grid-template-columns:repeat(3,12px);gap:24px 25px}
.dots span{width:12px;height:12px;border-radius:50%;background:#e2e2e2}
.review{position:absolute;top:2439px;width:329px;height:214px;background:#fff;box-shadow:0 18px 40px rgba(0,0,0,.07);padding:54px 30px 0 36px}
.review .avatar{position:absolute;top:-36px;left:41px;width:75px;height:75px;border-radius:50%}
.review p{font-size:14px;line-height:22.5px;color:var(--ink)}
.review .foot{position:absolute;left:36px;right:30px;bottom:14px;border-top:1px solid var(--line);padding-top:14px;display:flex;justify-content:space-between;align-items:center}
.review b{display:block;font-size:12px;font-weight:600;color:var(--ink)}
.review small{font-size:11.5px;color:var(--muted)}
.consult{position:absolute;left:183px;top:2764px;width:834px;height:241px;background:var(--sand);text-align:center}
.consult h2{margin-top:54px;font-weight:400;font-size:38px;line-height:40px;color:var(--ink)}
.consult p{margin:18px auto 0;width:660px;font-size:13px;line-height:22px;color:var(--ink)}
.consult p strong{font-weight:500;font-size:15px;border-bottom:1px solid var(--ink)}
.footer-brand{position:absolute;top:3070px;left:0;width:1200px;display:flex;flex-direction:column;align-items:center;gap:14px;color:var(--ink)}
.footer-brand .mark{width:90px;height:90px;border-radius:50%;background:var(--rose-soft)}
.footer-brand .name{font-family:'Alice',serif;font-size:38px;line-height:1;text-align:center}
.footer-brand .name small{display:block;font-size:24px;letter-spacing:5px}
.copyright{position:absolute;top:3398px;left:0;width:1200px;height:48px;background:#dcdcdc;text-align:center;line-height:48px;font-size:11.5px;font-weight:500;color:var(--ink)}
.totop{position:absolute;left:1128px;top:3370px;width:48px;height:48px;border-radius:50%;background:#fff;box-shadow:0 4px 14px rgba(0,0,0,.12);display:flex;align-items:center;justify-content:center}
</style>
</head>
<body>

<!-- header -->
<div class="social abs" style="left:90px;top:33px" aria-label="Social links"><span></span><span></span><span></span></div>
<div class="brand abs" style="left:462px;top:22px"><span class="mark"></span><span class="name">Stillwater<small>ACUPUNCTURE</small></span></div>
<div class="phone abs" style="left:960px;top:31px"><i><svg width="14" height="14" viewBox="0 0 24 24"><path fill="#555" d="M6.6 10.8a15 15 0 0 0 6.6 6.6l2.2-2.2c.3-.3.7-.4 1-.2 1.1.4 2.3.6 3.6.6.6 0 1 .4 1 1V20c0 .6-.4 1-1 1A17 17 0 0 1 3 4c0-.6.4-1 1-1h3.5c.6 0 1 .4 1 1 0 1.3.2 2.5.6 3.6.1.3 0 .7-.2 1z"/></svg></i>413-555-0148</div>
<div class="abs" style="left:0;top:96px;width:1200px;height:1px;background:var(--line)"></div>
<nav class="nav" style="top:118px"><span>HOME</span><span>ABOUT</span><span>FERTILITY &amp; PREGNANCY (NEST)</span><span>HORMONE BALANCE (ROCKS)</span><span>STRENGTH &amp; STRUCTURE (TREE)</span><span>EMOTIONAL WELLBEING (HEART)</span><span>ONLINE SHOP</span></nav>

<!-- hero -->
<section class="hero" role="img" aria-label="Photo of a smiling couple resting their heads together on a sofa">
  <div class="eyebrow">Welcome To</div>
  <h1>Philosophy<br>of Care</h1>
  <p>Acupuncture &amp; Chinese Herbal Medicine are rooted in over 3000 years of history and tradition. As a complete medical system that has remained flexible and relevant we honor what has worked from the past while embracing the medicine of tomorrow.</p>
  <div class="down"><svg width="24" height="28" viewBox="0 0 24 28"><path d="M12 2v23M3 16l9 9 9-9" fill="none" stroke="#555" stroke-width="1.6"/></svg></div>
</section>

<!-- mission -->
<div class="abs" style="left:568px;top:903px;width:64px;height:64px;border-radius:50%;background:var(--rose-soft)"></div>
<p class="quote">At Stillwater Acupuncture we provide compassionate, respectful and empowering care in a safe and inclusive environment. Our goal is to harmonize physical, mental and emotional wellbeing to strengthen the still point from which we all strive to live.</p>
<div class="rule"></div>

<!-- focus -->
<div class="band" style="top:1543px;height:689px"></div>
<h2 class="h2" style="top:1198px">Areas of focus</h2>
<div class="card" style="left:88px"><div class="pic" role="img" aria-label="Woman reading a pregnancy test" style="background:linear-gradient(135deg,#c9a79d,#7a5a52)"></div><h3>Fertility &amp; pregnancy</h3><p>At Stillwater Acupuncture our goal is to help build families and we happily embrace the...</p></div>
<div class="card" style="left:348px"><div class="pic" role="img" aria-label="Woman resting her head in her hand" style="background:linear-gradient(135deg,#e7dccb,#8791c4)"></div><h3>Emotional well being</h3><p>Our mental and emotional wellness is imperative to whole body healing. Without the unity of...</p></div>
<div class="card" style="left:606px"><div class="pic" role="img" aria-label="Bowls of herbs and grains" style="background:linear-gradient(135deg,#dcdfe6,#a48770)"></div><h3>Hormone balance</h3><p>Our hormones are constantly shifting and occasionally this internal orchestra needs to be refined...</p></div>
<div class="card" style="left:866px"><div class="pic" role="img" aria-label="Woman drinking water in a forest" style="background:linear-gradient(135deg,#8c6d4f,#e8dfd8)"></div><h3>Strength &amp; structure</h3><p>Our bodies carry us through all we do. Sometimes they need attention and support. Whether you...</p></div>

<!-- about -->
<section class="about">
  <div class="about-pic"></div>
  <div class="about-figure" role="img" aria-label="Pregnant woman in a knit dress holding her belly"></div>
  <div class="eyebrow">Introduction</div>
  <h2>About Maren</h2>
  <p>Maren Ashby is a Massachusetts and California Licensed Acupuncturist and Herbalist as well as Nationally Certified in both Acupuncture and Herbal Medicine. She obtained her Masters Degree from Seven Rivers University in Santa Cruz CA and has studied at the integrated hospital in Hang Zhou China. She has also done extensive study in Chi Nei Tsang in both the</p>
  <a>FIND OUT MORE</a>
</section>
<div class="dots"><span></span><span></span><span></span><span></span><span></span><span></span><span></span><span></span><span></span><span></span><span></span><span></span></div>

<!-- testimonials -->
<h2 class="h2" style="top:2320px">Testimonials</h2>
<svg width="0" height="0" style="position:absolute"><defs><path id="star" d="M8 0l2.4 5 5.6.6-4.2 3.8 1.2 5.6L8 12.2 3 15l1.2-5.6L0 5.6 5.6 5z"/></defs></svg>
<div class="review" style="left:88px"><div class="avatar" role="img" aria-label="Customer portrait" style="background:linear-gradient(135deg,#c58a6c,#5a3c31)"></div><p>Maren is one of the best acupuncturists I've been to in almost 20 years of on and off treatment. She is kind...</p><div class="foot"><div><b>DANA R.</b><small>Cambridge, MA</small></div><svg width="96" height="16"><use href="#star" fill="var(--gold)"/><use href="#star" x="19" fill="var(--gold)"/><use href="#star" x="38" fill="var(--gold)"/><use href="#star" x="57" fill="var(--gold)"/><use href="#star" x="76" fill="var(--gold-pale)"/></svg></div></div>
<div class="review" style="left:436px"><div class="avatar" role="img" aria-label="Customer portrait" style="background:linear-gradient(135deg,#8fb3c2,#2f3c43)"></div><p>Maren is truly a master of her craft. I had undergone years of infertility treatment, including two...</p><div class="foot"><div><b>LENA P.</b><small>Northampton, MA</small></div><svg width="96" height="16"><use href="#star" fill="var(--gold)"/><use href="#star" x="19" fill="var(--gold)"/><use href="#star" x="38" fill="var(--gold)"/><use href="#star" x="57" fill="var(--gold)"/><use href="#star" x="76" fill="var(--gold-pale)"/></svg></div></div>
<div class="review" style="left:783px"><div class="avatar" role="img" aria-label="Customer portrait" style="background:linear-gradient(135deg,#b3a49a,#4a3d36)"></div><p>Maren was absolutely wonderful! My first child was conceived through IVF. When we started talking...</p><div class="foot"><div><b>TESSA W.</b><small>Springfield, MA</small></div><svg width="96" height="16"><use href="#star" fill="var(--gold)"/><use href="#star" x="19" fill="var(--gold)"/><use href="#star" x="38" fill="var(--gold)"/><use href="#star" x="57" fill="var(--gold)"/><use href="#star" x="76" fill="var(--gold-pale)"/></svg></div></div>

<!-- consultation + footer -->
<div class="band" style="top:2890px;height:508px"></div>
<div class="consult">
  <h2>Schedule a free 30 minute<br>consultation</h2>
  <p>Consultations are always available to help answer any questions you may have about acupuncture or herbal medicine in a relaxed environment. <strong>413-555-0148</strong></p>
</div>
<div class="footer-brand"><span class="mark"></span><span class="name">Stillwater<small>ACUPUNCTURE</small></span></div>
<nav class="nav" style="top:3252px"><span>HOME</span><span>ABOUT</span><span>FERTILITY &amp; PREGNANCY (NEST)</span><span>HORMONE BALANCE (ROCKS)</span><span>STRENGTH &amp; STRUCTURE (TREE)</span><span>EMOTIONAL WELLBEING (HEART)</span><span>ONLINE SHOP</span></nav>
<div class="social abs" style="left:537px;top:3293px" aria-label="Social links"><span style="background:#e8e4e3"></span><span style="background:#e8e4e3"></span><span style="background:#e8e4e3"></span></div>
<div class="copyright">COPYRIGHT © 2020 STILLWATER ACUPUNCTURE</div>
<div class="totop"><svg width="14" height="18" viewBox="0 0 14 18"><path d="M7 17V1M1 7l6-6 6 6" fill="none" stroke="#555" stroke-width="1.3"/></svg></div>

</body>
</html>
```